Visitenkarten-Design für Lichtfeder - Zeilen von Hand zu Hand
Zielgruppe
Ich schreibe Briefe an Menschen, die mehr über sich erfahren wollen, die sich berühren lassen wollen, die an sich arbeiten möchten, die sich entfalten wollen. Ich möchte nicht den Verstand sondern das Herz ansprechen, die Selbstheilung erfahren möchten, damit sie Impulse bekommen, um ein glücklicheres Leben zu führen, das ihnen mehr entspricht.
Ich sehe mich als Mensch, der andere Menschen in ihrem Leben unterstützen möchte.
Aufgabenstellung
Die Briefe schreibe ich in Segoe Print, goldene Schrift auf gelblichem Papier, evtl auch anderes Papier, wenn die goldene Schrift passt.
Die Visitenkarte sollte Freude, Freiheit und Anerkennung des Menschen an sich ausstrahlen. Farben evtl. Bordeaux, mit vielleicht Rosa. Sie sollte jedoch nicht kitschig wirken.
Schön wäre vielleicht etwas mit Blumen oder Ornamenten, jedoch nicht zu überladen.
Als Text soll drauf sein:
Das beigefügte Logo, dann:
Berühren - Bewegen - Begeistern

```html
<!DOCTYPE html>
<html lang="de">
<head>
<meta charset="utf-8">
<title>Lichtfeder – Berühren, Bewegen, Begeistern</title>
<link rel="stylesheet" href="https://fonts.googleapis.com/css2?family=Great+Vibes&display=swap">
<style>
  :root {
    --paper: #fde3e1;
    --bordeaux: #6c0c2b;
    --bordeaux-deep: #5e0a25;
    --blush-fade: rgba(253, 227, 225, 0);
  }
  html, body {
    margin: 0;
    padding: 0;
    width: 1200px;
    height: 763px;
    overflow: hidden;
    background: var(--paper);
  }
  .card {
    position: relative;
    width: 1200px;
    height: 763px;
    overflow: hidden;
    background: var(--paper);
    font-family: "Great Vibes", cursive;
    color: var(--bordeaux);
  }
  .glow {
    position: absolute;
    left: -404px;
    top: 181px;
    width: 1000px;
    height: 1000px;
    border-radius: 50%;
    background: radial-gradient(circle at center,
      var(--bordeaux-deep) 0%,
      rgba(108, 12, 43, 0.85) 18%,
      rgba(150, 60, 85, 0.55) 38%,
      rgba(220, 170, 178, 0.25) 55%,
      var(--blush-fade) 68%);
  }
  .mission {
    position: absolute;
    right: 178px;
    top: 88px;
    margin: 0;
    text-align: right;
    font-size: 58px;
    font-weight: 400;
    line-height: 88px;
    letter-spacing: 0;
  }
  .mission span { display: block; white-space: nowrap; }
  .tagline {
    position: absolute;
    right: 178px;
    top: 508px;
    margin: 0;
    font-size: 60px;
    font-weight: 400;
    white-space: nowrap;
  }
  .floral-ornament {
    position: absolute;
    right: 0;
    bottom: 0;
    width: 245px;
    height: 345px;
    border-top-left-radius: 70% 60%;
    background: radial-gradient(ellipse at 75% 70%,
      rgba(108, 12, 43, 0.75) 0%,
      rgba(108, 12, 43, 0.45) 45%,
      rgba(108, 12, 43, 0) 75%);
  }
</style>
</head>
<body>
  <main class="card">
    <div class="glow"></div>
    <p class="mission">
      <span>Mein Anliegen ist es, Sie zu begeistern,</span>
      <span>damit Sie Begeisterung über Sich selbst</span>
      <span>erkennen und erfahren.</span>
    </p>
    <p class="tagline">Berühren - Bewegen - Begeistern</p>
    <div class="floral-ornament" role="img" aria-label="Bordeauxrote Blumenranke mit Blüten und Blättern"></div>
  </main>
</body>
</html>
```